Brisket Vantle Orbis Holdings.com

We are doing a full website redesign. Here is a video explanation of what we need https://www.clipvessa.com/share/4b21f09a6ce347d1a85f2e7b90d15c66

THANK YOU SO MUCH!!

Here is a link to our current site
http://www.qentrifold.com

Target Market(s)

Pelwick QRX Sellers

Number of Pages Required

5+ page

Requirements
Must have
• Watch the video and follow the instructions!
• https://www.clipvessa.com/share/4b21f09a6ce347d1a85f2e7b90d15c66

```html
<!DOCTYPE html>
<html lang="en">
<head>
<meta charset="utf-8">
<title>Qentrifold.com – Member Area</title>
<link rel="stylesheet" href="https://fonts.googleapis.com/css2?family=Montserrat:wght@400;500;600;700&display=swap">
<style>
  :root {
    --backdrop: #fcc7c7;
    --red: #fe1b1d;
    --ink: #1a1a1a;
    --muted: #8a8a8a;
    --line: #d0d0d0;
    --card-top: #ececec;
    --bar: #000000;
    --white: #ffffff;
    --green: #2fb34a;
  }
  * { box-sizing: border-box; margin: 0; padding: 0; }
  html, body { width: 837px; height: 1200px; overflow: hidden; }
  body {
    background: var(--backdrop);
    font-family: "Montserrat", sans-serif;
    color: var(--ink);
    position: relative;
  }

  /* ---------- Login screen ---------- */
  .login-screen {
    position: absolute; left: 83px; top: 47px; width: 670px; height: 383px;
    overflow: hidden; box-shadow: 0 2px 6px rgba(0,0,0,.15);
  }
  .city-backdrop {
    position: absolute; inset: 0;
    background: linear-gradient(180deg, #2c2f6e 0%, #4a4b8a 30%, #6b5a8e 48%, #2e3a66 62%, #1e2748 80%, #151b33 100%);
  }
  .login-card {
    position: absolute; left: 197px; top: 66px; width: 276px; height: 250px;
    background: var(--white); border-radius: 2px;
  }
  .login-card .site-name {
    position: absolute; top: 30px; width: 100%; text-align: center;
    font-size: 18.5px; font-weight: 600;
  }
  .field {
    position: absolute; left: 37px; width: 202px; height: 20px;
    border-bottom: 1px solid var(--line);
    display: flex; align-items: center; gap: 7px;
    font-size: 7px; color: var(--muted);
  }
  .field.email { top: 82px; }
  .field.password { top: 115px; }
  .remember {
    position: absolute; left: 37px; top: 149px;
    display: flex; align-items: center; gap: 5px;
    font-size: 7px; color: var(--muted);
  }
  .remember .box { width: 8px; height: 8px; border: 1px solid #999; border-radius: 1px; }
  .login-button {
    position: absolute; left: 45px; top: 184px; width: 186px; height: 33px;
    background: var(--red); color: var(--white);
    font-size: 9.5px; font-weight: 600;
    display: flex; align-items: center; justify-content: center;
  }

  /* ---------- Dashboard ---------- */
  .dashboard {
    position: absolute; left: 85px; top: 464px; width: 670px; height: 698px;
    background: var(--white); box-shadow: 0 2px 6px rgba(0,0,0,.12);
  }
  .top-bar {
    height: 38px; background: var(--bar); color: var(--white);
    position: relative;
  }
  .top-bar .site-name {
    position: absolute; left: 61px; top: 11px; font-size: 14px; font-weight: 700;
  }
  .main-nav {
    position: absolute; left: 325px; top: 0; height: 38px;
    display: flex; align-items: center; gap: 10px;
    font-size: 7px; font-weight: 500;
  }
  .main-nav span { display: flex; align-items: center; gap: 3px; }
  .main-nav .caret { font-size: 5px; margin-left: 2px; }
  .search-icon { position: absolute; left: 596px; top: 14px; }

  .section-title {
    position: absolute; width: 100%; text-align: center;
    font-size: 19px; font-weight: 600;
  }
  .section-title.programs { top: 80px; }
  .section-title.bonuses { top: 501px; }

  .program-card {
    position: absolute; background: var(--white);
    box-shadow: 0 1px 3px rgba(0,0,0,.18);
    text-align: center;
  }
  .program-card.starter { left: 61px; top: 148px; width: 178px; height: 274px; }
  .program-card.elite   { left: 244px; top: 137px; width: 177px; height: 302px; }
  .program-card.eight   { left: 427px; top: 148px; width: 178px; height: 274px; }

  .card-head { position: absolute; left: 0; top: 0; width: 100%; }
  .card-head svg { display: block; }
  .card-head .head-label {
    position: absolute; left: 0; width: 100%; text-align: center;
    font-size: 15px; font-weight: 500;
  }
  .elite .head-label { color: var(--white); top: 33px; }
  .eight .head-label, .starter .head-label { color: var(--ink); top: 30px; }

  .card-title { position: absolute; width: 100%; font-size: 12px; font-weight: 500; }
  .starter .card-title, .eight .card-title { top: 92px; }
  .elite .card-title { top: 107px; }

  .progress-note { position: absolute; top: 115px; width: 100%; font-size: 6.5px; font-weight: 500; }
  .progress-track {
    position: absolute; left: 43px; top: 130px; width: 93px; height: 2px; background: #e6e6e6;
  }
  .progress-track .fill { width: 22%; height: 100%; background: var(--green); }

  .card-copy {
    position: absolute;
    font-size: 7.2px; line-height: 14.2px; color: var(--muted);
  }
  .starter .card-copy { left: 19px; width: 140px; top: 151px; }
  .eight .card-copy { left: 26px; width: 126px; top: 151px; }
  .elite .card-copy { left: 25px; width: 127px; top: 176px; }

  .card-button {
    position: absolute; height: 30px;
    display: flex; align-items: center; justify-content: center;
    font-size: 8.5px; font-weight: 500; color: var(--white); background: var(--ink);
  }
  .starter .card-button, .eight .card-button { left: 30px; top: 217px; width: 118px; }
  .elite .card-button.small { left: 42px; top: 133px; width: 93px; height: 23px; font-size: 7.5px; border: 1px solid #000; }
  .elite .card-button.primary { left: 29px; top: 245px; width: 118px; background: var(--red); }

  .lock-badge {
    position: absolute; left: 78px; top: 116px; width: 22px; height: 22px; border-radius: 50%;
    background: var(--ink); display: flex; align-items: center; justify-content: center;
  }

  .bonus {
    position: absolute; top: 573px; display: flex; align-items: center; gap: 11px;
    font-size: 12.5px; line-height: 19px; color: #555;
  }
  .bonus.ads { left: 92px; }
  .bonus.picks { left: 292px; }
  .bonus.package { left: 531px; }
  .bonus .badge {
    width: 37px; height: 37px; border-radius: 50%; background: var(--red);
    display: flex; align-items: center; justify-content: center; flex-shrink: 0;
  }

  .footer-note {
    position: absolute; top: 670px; width: 100%; text-align: center;
    font-size: 8px; font-weight: 500;
  }
</style>
</head>
<body>

<section class="login-screen">
  <div class="city-backdrop" role="img" aria-label="Evening city skyline photograph under a purple sky"></div>
  <form class="login-card">
    <h1 class="site-name">Qentrifold.com</h1>
    <div class="field email">
      <svg width="12" height="9" viewBox="0 0 12 9" fill="none" stroke="#777" stroke-width="1"><rect x="0.5" y="0.5" width="11" height="8"/><path d="M0.5 0.5 L6 5 L11.5 0.5"/></svg>
      Email
    </div>
    <div class="field password">
      <svg width="9" height="11" viewBox="0 0 9 11" fill="none" stroke="#777" stroke-width="1"><rect x="0.5" y="4.5" width="8" height="6"/><path d="M2 4.5 V3 a2.5 2.5 0 0 1 5 0 V4.5"/></svg>
      Password
    </div>
    <label class="remember"><span class="box"></span>Remember Me</label>
    <div class="login-button">Log In</div>
  </form>
</section>

<main class="dashboard">
  <header class="top-bar">
    <div class="site-name">Qentrifold.com</div>
    <nav class="main-nav">
      <span><svg width="9" height="8" viewBox="0 0 10 9"><path d="M5 9 L0.8 4.6 A2.4 2.4 0 0 1 5 1.6 A2.4 2.4 0 0 1 9.2 4.6 Z" fill="#fe1b1d"/></svg>Refer a friend</span>
      <span><svg width="7" height="8" viewBox="0 0 7 8" fill="#fff"><circle cx="3.5" cy="2" r="2"/><path d="M0 8 a3.5 3.5 0 0 1 7 0 Z"/></svg>Hi Dorin!<span class="caret">▼</span></span>
      <span><svg width="9" height="8" viewBox="0 0 9 8" fill="#fff"><path d="M4.5 0 L9 4 H7.5 V8 H5.5 V5.5 H3.5 V8 H1.5 V4 H0 Z"/></svg>Community<span class="caret">▼</span></span>
      <span><svg width="8" height="8" viewBox="0 0 8 8" fill="none" stroke="#fff" stroke-width="0.9"><circle cx="4" cy="4" r="3.5"/><ellipse cx="4" cy="4" rx="1.6" ry="3.5"/><path d="M0.5 4 H7.5"/></svg>Help<span class="caret">▼</span></span>
    </nav>
    <svg class="search-icon" width="10" height="10" viewBox="0 0 10 10" fill="none" stroke="#fff" stroke-width="1.5"><circle cx="4" cy="4" r="3"/><path d="M6.3 6.3 L9.3 9.3"/></svg>
  </header>

  <h2 class="section-title programs">Your Training Programs</h2>

  <article class="program-card starter">
    <div class="card-head">
      <svg width="178" height="81" viewBox="0 0 178 81"><path d="M0 0 H178 V72 Q89 90 0 72 Z" fill="#ececec"/></svg>
      <div class="head-label">Qentri U 2.0</div>
    </div>
    <h3 class="card-title">Qentrifold University 2.0</h3>
    <p class="progress-note">10% Complete</p>
    <div class="progress-track"><div class="fill"></div></div>
    <p class="card-copy">How To Start nad Grow a 6-Figure Pelwick QRX BUsiness With focus on correctly Dominating with one product</p>
    <div class="card-button">Continue Lesson</div>
  </article>

  <article class="program-card elite">
    <div class="card-head">
      <svg width="177" height="90" viewBox="0 0 177 90"><path d="M0 0 H177 V77 Q88 97 0 77 Z" fill="#fe1b1d"/></svg>
      <div class="head-label">Qentri U Elite</div>
    </div>
    <h3 class="card-title">Qentri U Elite</h3>
    <div class="card-button small">Continue Lesson</div>
    <p class="card-copy">Competely Dominate Multiple Markets,Make 8 Figures and Eventually Sell Your Empire For a Huge Cash Exit</p>
    <div class="card-button primary">Continue Lesson</div>
  </article>

  <article class="program-card eight">
    <div class="card-head">
      <svg width="178" height="81" viewBox="0 0 178 81"><path d="M0 0 H178 V72 Q89 90 0 72 Z" fill="#ececec"/></svg>
      <div class="head-label">Qentri U Eight</div>
    </div>
    <h3 class="card-title">Qentri U Eight</h3>
    <div class="lock-badge">
      <svg width="8" height="10" viewBox="0 0 9 11" fill="none" stroke="#fff" stroke-width="1"><rect x="0.5" y="4.5" width="8" height="6"/><path d="M2 4.5 V3 a2.5 2.5 0 0 1 5 0 V4.5"/></svg>
    </div>
    <p class="card-copy">Competely Dominate Multiple Markets,Make 8 Figures and Eventually Sell Your Empire For a Huge Cash Exit</p>
    <div class="card-button">Coming Soon</div>
  </article>

  <h2 class="section-title bonuses">Your V.I.P Bonuses</h2>

  <div class="bonus ads">
    <span class="badge"><svg width="18" height="14" viewBox="0 0 18 14" fill="none" stroke="#fff" stroke-width="3"><path d="M2 7 L7 12 L16 2"/></svg></span>
    <span>Qentri U Chirplet<br>Ads</span>
  </div>
  <div class="bonus picks">
    <span class="badge"><svg width="11" height="14" viewBox="0 0 9 11" fill="none" stroke="#fff" stroke-width="1"><rect x="0.5" y="4.5" width="8" height="6"/><path d="M2 4.5 V3 a2.5 2.5 0 0 1 5 0 V4.5"/><path d="M4.5 6.5 V8.5"/></svg></span>
    <span>RV Approved Product<br>Pick List</span>
  </div>
  <div class="bonus package">
    <span class="badge"><svg width="15" height="15" viewBox="0 0 15 15" fill="none" stroke="#fff" stroke-width="1.3"><rect x="1" y="6.5" width="3" height="7"/><path d="M4 7 L7 1.5 Q8.5 1.5 8.5 3.5 L8 6 H12.5 Q14 6 13.6 7.6 L12.4 12.4 Q12 13.5 10.8 13.5 H4"/></svg></span>
    <span>All In One<br>Package</span>
  </div>

  <footer class="footer-note">Copyrights © 2019 | All Rights Reserved</footer>
</main>

</body>
</html>
```